Business card for new Kids Clothing Company
Dapple Togs
Bright & Fun-filled
Hannah Pryce, MBA
Owner
PO Box 863 West Marlowe, PA 17093
hannah@dappletogs.com
www.dappletogs.com
our tag line is: Soft clothing designed with sensitive kids in mind, made for ALL!
Xpert Xpert
oncdoc15 oncdoc15
All, I am looking for a business card AND letterhead also, please try to keep the cards to ONE side only thanks

```html
<!DOCTYPE html>
<html lang="en">
<head>
<meta charset="utf-8">
<title>Dapple Togs – Business Card</title>
<link rel="stylesheet" href="https://fonts.googleapis.com/css2?family=Open+Sans:ital,wght@0,400;0,600;0,700;1,700&display=swap">
<style>
  :root {
    --backdrop: #3b3b3d;
    --pink-light: #f4479f;
    --pink-deep: #e0137c;
    --tagline-yellow: #ffe23a;
    --white: #ffffff;
    --paper-light: #fbfbfb;
    --paper-shade: #e4e4e4;
    --ink-grey: #6a6a6a;
    --rule-grey: #cfcfcf;
  }
  * { margin: 0; padding: 0; box-sizing: border-box; }
  html, body {
    width: 1200px; height: 1099px; overflow: hidden;
    background: var(--backdrop);
    font-family: "Open Sans", Arial, sans-serif;
  }
  .canvas { position: relative; width: 1200px; height: 1099px; }

  .card {
    position: absolute;
    width: 780px; height: 394px;
    border-radius: 30px;
    overflow: hidden;
    box-shadow: 0 10px 24px rgba(0,0,0,.35);
  }

  /* Front */
  .card-front {
    left: 352px; top: 113px;
    background: radial-gradient(ellipse at 50% 40%, var(--pink-light) 0%, var(--pink-deep) 85%);
    color: var(--white);
    text-align: center;
  }
  .brand-mark {
    position: absolute; left: 0; right: 0; top: 150px;
    display: flex; align-items: center; justify-content: center; gap: 16px;
  }
  .brand-dot {
    width: 40px; height: 40px; border-radius: 50%;
    background: var(--white);
  }
  .brand-name {
    font-weight: 700; font-size: 52px; letter-spacing: 1px;
    color: var(--white);
  }
  .front-tagline {
    position: absolute; left: 0; right: 0; top: 297px;
    font-weight: 700; font-style: italic; font-size: 19px;
    color: var(--tagline-yellow);
  }
  .front-web {
    position: absolute; left: 0; right: 0; top: 332px;
    font-weight: 600; font-size: 14px;
  }

  /* Back */
  .card-back {
    left: 72px; top: 592px;
    background: linear-gradient(180deg, var(--paper-light) 0%, var(--paper-shade) 100%);
    color: var(--ink-grey);
  }
  .back-brand {
    position: absolute; left: 46px; top: 70px;
    display: flex; align-items: center; gap: 12px;
  }
  .back-brand .brand-dot { width: 30px; height: 30px; background: var(--pink-deep); }
  .back-brand .brand-name { font-size: 38px; color: var(--pink-deep); }
  .back-rule {
    position: absolute; left: 0; right: 0; top: 206px; height: 2px;
    background: linear-gradient(90deg, var(--rule-grey), var(--pink-light) 60%, var(--rule-grey));
  }
  .person {
    position: absolute; right: 62px; top: 216px; text-align: right;
  }
  .person-name { font-size: 23px; font-weight: 600; color: var(--pink-deep); }
  .person-name .credential { color: var(--ink-grey); }
  .person-role { font-size: 14px; margin-top: 1px; }
  .contact {
    position: absolute; left: 46px; top: 306px;
    font-size: 14px; line-height: 19px; font-style: normal;
  }
  .back-band {
    position: absolute; left: 0; right: 0; bottom: 0; height: 11px;
    background: var(--pink-deep);
  }
</style>
</head>
<body>
<main class="canvas">
  <section class="card card-front" aria-label="Business card front">
    <div class="brand-mark">
      <span class="brand-dot"></span>
      <span class="brand-name">Dapple Togs</span>
    </div>
    <p class="front-tagline">Soft clothing designed with sensitive kids in mind, made for ALL!</p>
    <p class="front-web">www.dappletogs.com</p>
  </section>

  <section class="card card-back" aria-label="Business card back">
    <div class="back-brand">
      <span class="brand-dot"></span>
      <span class="brand-name">Dapple Togs</span>
    </div>
    <div class="back-rule"></div>
    <div class="person">
      <p class="person-name">Hannah Pryce<span class="credential">, MBA</span></p>
      <p class="person-role">Owner</p>
    </div>
    <address class="contact">
      PO Box 863, West Marlowe, PA 17093<br>
      P: (717) 555-0148, E: hannah@dappletogs.com<br>
      www.dappletogs.com
    </address>
    <div class="back-band"></div>
  </section>
</main>
</body>
</html>
```